Design for new site

Hi, we need a web design for a new product calmridgeway.
This product is aimed to help people with anxiety, panic attacks and other disorders on permanently basis.
Please take a look at competitors web-sites:
http://www.brightharborpath.example/
http://www.stillmeadow.example/
Key Audiences
The intended audience for this site will be people that are looking for relief from panic and anxiety.
Key Objectives
Key object is to get prospective clients to sign up for membership and purchase our audio course.
Theme of Site
The general site theme needs to be clean and simple. The audience coming to the site in under a lot of anxiety and we don’t want to add any stress.
The site needs to flow easy from top down, with few distractions in side menus and/or columns.
Color Scheme
Suggested colors need to be light shades of blue. Blue psychology is tranquil, peaceful, and calm. This color has a tremendous stress management quality to it, making us feel cool and calm.
Or it can be shades of cool green of summer forest.
Please take a look at site mock up in attachment.

```html
<!DOCTYPE html>
<html lang="en">
<head>
<meta charset="utf-8">
<title>calmridgeway</title>
<link href="https://fonts.googleapis.com/css2?family=Open+Sans:wght@400;600;700&display=swap" rel="stylesheet">
<style>
:root{
  --sky-top:#3fc2f0;
  --sky-bottom:#9fe3fb;
  --navy:#1b3a6b;
  --blue:#1e8fd0;
  --blue-dark:#1476b3;
  --slide-bg:#2d3138;
  --slide-text:#8fd2f3;
  --text:#5d6470;
  --heading:#2b5a86;
  --rule:#d5dbe1;
  --field:#ffffff;
  --field-border:#c6d2dc;
  --footer:#333538;
  --footer-text:#ffffff;
  --muted:#9aa3ab;
}
*{box-sizing:border-box;margin:0;padding:0}
html,body{width:893px;height:1200px;overflow:hidden}
body{position:relative;background:#fff;font-family:"Open Sans",Arial,sans-serif;color:var(--text)}
.abs{position:absolute}

/* hero */
.hero{left:0;top:0;width:893px;height:357px;background:linear-gradient(180deg,var(--sky-top) 0%,var(--sky-bottom) 100%)}
.hero::after{content:"";position:absolute;left:0;right:0;bottom:-10px;height:10px;background:linear-gradient(180deg,rgba(0,0,0,.08),rgba(0,0,0,0))}
.brand{left:90px;top:26px;height:46px;display:flex;align-items:center;gap:10px}
.brand-mark{width:22px;height:22px;background:var(--navy)}
.brand-name{font-size:22px;font-weight:700;color:#fff;letter-spacing:.5px}
.nav{left:333px;top:40px;display:flex;gap:20px;font-size:11.5px;font-weight:700;color:#fff}
.nav a{color:#fff;text-decoration:none;position:relative}
.nav a.active::after{content:"";position:absolute;left:50%;top:22px;margin-left:-5px;border:5px solid transparent;border-bottom:6px solid #fff}
.slide{left:120px;top:125px;width:216px;height:193px;background:var(--slide-bg);padding:18px 18px}
.slide h1{font-size:20px;font-weight:700;color:#fff;line-height:1.2}
.slide p{font-size:10px;color:var(--slide-text);line-height:1.35;margin-top:10px}
.btn{display:inline-block;background:var(--blue);color:#fff;font-weight:700;font-size:10.5px;padding:6px 12px;border-radius:2px}
.slide .btn{margin-top:14px}
.dots{display:flex;gap:5px;margin-top:10px}
.dots span{width:6px;height:6px;border-radius:50%;background:#6c737c}
.dots span.on{background:var(--blue)}
.hero-photo{left:476px;top:118px;width:254px;height:239px;background:linear-gradient(180deg,#b9c3cc,#7d8791)}
.arrow{width:32px;height:32px;border-radius:50%;background:rgba(255,255,255,.85);border:1px solid #d6e4ec;top:195px}
.arrow svg{position:absolute;left:9px;top:8px}

/* intro */
.intro{left:90px;top:417px;width:445px;font-size:10.5px;line-height:1.5}
.intro p+p{margin-top:12px}
.signup{left:575px;top:387px;width:230px;height:178px;background:var(--sky-bottom);background:linear-gradient(180deg,#8fdaf7,#4cc4ef)}
.signup-head{background:var(--blue);color:#fff;font-size:16px;font-weight:700;padding:8px 18px;height:36px}
.field{display:block;background:var(--field);border:1px solid var(--field-border);font-size:9px;color:var(--muted);padding:5px 8px;height:22px;border-radius:2px}
.signup .field{width:160px;margin:12px 0 0 20px}
.signup .btn{margin:14px 0 0 20px;padding:7px 12px}

/* section headings */
.section-title{font-size:15px;font-weight:600;color:var(--heading)}
.rule{height:1px;background:var(--rule)}
.mini-arrows{display:flex;gap:4px}
.mini-arrows span{width:13px;height:13px;border-radius:50%;background:#b6c1c9;position:relative}
.mini-arrows svg{position:absolute;left:3px;top:3px}

/* blog */
.blog-photo{left:90px;top:662px;width:178px;height:143px;background:linear-gradient(180deg,#9bb48e,#6a7d63)}
.article{left:289px;top:668px;width:246px}
.article h3{font-size:17px;font-weight:400;color:var(--blue)}
.article p{font-size:10.5px;line-height:1.45;margin-top:6px}

/* about */
.about-title{left:90px;top:884px}
.about-title strong{color:var(--blue);font-weight:600}
.about{left:90px;top:915px;width:445px;font-size:10.5px;line-height:1.5}
.about-btn{left:90px;top:1016px;padding:8px 14px;font-size:11px}

/* testimonials */
.testimonial{left:575px;width:230px;display:flex;gap:10px}
.avatar{width:34px;height:34px;border-radius:50%;flex:none;background:linear-gradient(180deg,#c9d0d6,#8e979f)}
.quote{font-size:8.5px;line-height:1.4}
.quote cite{display:block;font-style:normal;color:var(--blue);margin-top:3px;text-align:right}

/* newsletter */
.news-text{left:575px;top:915px;width:225px;font-size:10px;line-height:1.45}
.news-text strong{color:var(--blue);font-weight:600}
.news-field{left:575px;width:228px}
.news-btn{left:575px;top:1058px;padding:5px 9px;font-size:10px}

/* footer */
.footer{left:0;top:1120px;width:893px;height:80px;background:var(--footer)}
.footer-links{left:90px;top:1145px;display:flex;gap:13px;font-size:10.5px;font-weight:700;color:var(--footer-text)}
.copyright{left:90px;top:1163px;font-size:8.5px;color:#c3c7cb}
.social{left:710px;top:1145px;display:flex;gap:10px}
.social span{width:18px;height:18px;border-radius:2px;background:#3b8fd4}
.social span.red{background:#c43b35}
</style>
</head>
<body>

<header class="abs hero">
  <div class="abs brand"><span class="brand-mark"></span><span class="brand-name">YOUR LOGO</span></div>
  <nav class="abs nav">
    <a class="active">Home</a><a>Product</a><a>Success Stories</a><a>Anxiety Test</a><a>Blog</a><a>About</a><a>FAQ</a><a>Contact Us</a>
  </nav>
  <div class="abs slide">
    <h1>Lorem Ipsum Dolor</h1>
    <p>Ut enim ad minim veniam, quis nostrud exercitation ullamco laboris nisi ut aliquip ex ea commodo consequat. Duis aute irure.</p>
    <span class="btn">Learn More</span>
    <div class="dots"><span class="on"></span><span></span><span></span><span></span></div>
  </div>
  <div class="abs hero-photo" role="img" aria-label="Photo of two people, one calming the other"></div>
  <div class="abs arrow" style="left:34px"><svg width="14" height="16" viewBox="0 0 14 16"><path d="M10 2 L4 8 L10 14" fill="none" stroke="#9aa6b0" stroke-width="2"/></svg></div>
  <div class="abs arrow" style="left:826px"><svg width="14" height="16" viewBox="0 0 14 16"><path d="M4 2 L10 8 L4 14" fill="none" stroke="#9aa6b0" stroke-width="2"/></svg></div>
</header>

<section class="abs intro">
  <p>Lorem ipsum dolor sit amet, consectetur adipiscing elit, sed do eiusmod tempor incididunt ut labore et dolore magna aliqua. Ut enim ad minim veniam, quis nostrud exercitation ullamco laboris nisi ut aliquip ex ea commodo consequat.</p>
  <p>Labore et dolore magna aliqua. Ut enim ad minim veniam, quis nostrud exercitation ullamco laboris nisi ut aliquip ex ea commodo consequat. Duis aute irure dolor in reprehenderit in.</p>
</section>

<aside class="abs signup">
  <div class="signup-head">Sign Up Now!</div>
  <span class="field">Enter your name</span>
  <span class="field">Enter your email</span>
  <span class="btn">Submit</span>
</aside>

<h2 class="abs section-title" style="left:90px;top:625px">Blog</h2>
<div class="abs rule" style="left:130px;top:636px;width:370px"></div>
<div class="abs mini-arrows" style="left:505px;top:630px">
  <span><svg width="7" height="7" viewBox="0 0 7 7"><path d="M5 0.5 L2 3.5 L5 6.5" fill="none" stroke="#fff" stroke-width="1.5"/></svg></span>
  <span><svg width="7" height="7" viewBox="0 0 7 7"><path d="M2 0.5 L5 3.5 L2 6.5" fill="none" stroke="#fff" stroke-width="1.5"/></svg></span>
</div>
<div class="abs blog-photo" role="img" aria-label="Photo of a man sitting on a park bench"></div>
<article class="abs article">
  <h3>Title of article here</h3>
  <p>Consectetur adipiscing elit, sed do eiusmod tempor incididunt ut labore et dolore magna aliqua. Ut enim ad minim veniam, quis nostrud exercitation ullamco laboris nisi ut aliquip ex ea commodo.</p>
</article>

<h2 class="abs section-title about-title">About <strong>calmridgeway</strong></h2>
<p class="abs about">Labore et dolore magna aliqua. Ut enim ad minim veniam, quis nostrud exercitation ullamco laboris nisi ut aliquip ex ea commodo consequat. Duis aute irure dolor in reprehenderit in, voluptate velit esse cillum dolore eu fugiat nulla pariatur. Excepteur sint occaecat cupidatat.</p>
<span class="abs btn about-btn">Read More</span>

<h2 class="abs section-title" style="left:575px;top:625px">Testimonials</h2>
<div class="abs mini-arrows" style="left:770px;top:630px">
  <span><svg width="7" height="7" viewBox="0 0 7 7"><path d="M5 0.5 L2 3.5 L5 6.5" fill="none" stroke="#fff" stroke-width="1.5"/></svg></span>
  <span><svg width="7" height="7" viewBox="0 0 7 7"><path d="M2 0.5 L5 3.5 L2 6.5" fill="none" stroke="#fff" stroke-width="1.5"/></svg></span>
</div>
<div class="abs testimonial" style="top:668px">
  <div class="avatar" role="img" aria-label="Portrait photo of a male customer"></div>
  <p class="quote">The daily audio lessons helped me breathe again. I finally sleep through the night and feel in control of my mornings.<cite>— Mark D.</cite></p>
</div>
<div class="abs testimonial" style="top:765px">
  <div class="avatar" role="img" aria-label="Portrait photo of a female customer"></div>
  <p class="quote">After years of sudden panic, this course gave me calm tools I use every day at work and at home.<cite>— Laura S.</cite></p>
</div>
<div class="abs rule" style="left:575px;top:858px;width:230px"></div>

<h2 class="abs section-title" style="left:575px;top:884px">Newsletter</h2>
<p class="abs news-text">Sign up to our newsletter to receive discounts, news and updates from <strong>calmridgeway</strong></p>
<span class="abs field news-field" style="top:982px">Name</span>
<span class="abs field news-field" style="top:1016px">Email</span>
<span class="abs btn news-btn">Subscribe</span>

<footer class="abs footer"></footer>
<nav class="abs footer-links"><span>Home</span><span>Product</span><span>Success Stories</span><span>Anxiety Test</span><span>Blog</span><span>About</span><span>FAQ</span><span>Contact Us</span></nav>
<p class="abs copyright">Copyright © calmridgeway. All Rights Reserved.</p>
<div class="abs social"><span></span><span></span><span></span><span class="red"></span></div>

</body>
</html>
```